Cryptocurrency Advisor Business Card

Dravelin Consulting Services is my company, which advises many projects in the ICO/Cryptocurrency industry. I'd like to get a sleek, preferably matte black or matte dark blue finish, business card with the company name (and simple logo w/ crypto feel) on one side and while the other side I'd like a small twitter and telegram logo together maybe separated by a / as it's the same, then an email and a phone logo so I can insert those specifics there (no address). Can have name then CEO section too. At the bottom of that section, find a place for more of a job description: ICO Advisor, World Champion Gamer, Esports Award Winner, Quorvane Expert. You can possibly design a simple logo or use something with a crypto twist or background, but nothing too complex. Rounded edges for printing not square.
Updates

Had personal issues taking a few days away from me being able to provide feedback and check designs, etc. Will be more active now finalizing design just needed few days from issue but all is sorted.

Target Market(s)

Cryptocurrency industry

Industry/Entity Type

Management Consulting

Contact Information for Business Card

Font styles to use
Sans Serif

Colors
5c5c5c
474747
757575
9d9d9d
aaaaaa
333333
0355a3

Requirements
Must have
• Refer to Details/Description
Nice to have
Should not have
• Address section

```html
<!DOCTYPE html>
<html lang="en">
<head>
<meta charset="utf-8">
<title>Dravelin Consulting – Business Card</title>
<link rel="stylesheet" href="https://fonts.googleapis.com/css2?family=Lato:ital,wght@0,400;0,700;0,900;1,700&display=swap">
<style>
  :root {
    --backdrop: #333333;
    --card-navy: #022a5a;
    --card-black: #161616;
    --ink-white: #ffffff;
    --ink-soft: #d6d6d6;
    --ink-muted: #aaaaaa;
  }
  * { box-sizing: border-box; margin: 0; padding: 0; }
  html, body { width: 1200px; height: 782px; overflow: hidden; }
  body {
    background: var(--backdrop);
    font-family: "Lato", sans-serif;
    position: relative;
  }
  .card {
    position: absolute;
    width: 560px;
    height: 320px;
    border-radius: 14px;
    box-shadow: 0 14px 30px rgba(0,0,0,0.45);
  }
  .card-front { left: 560px; top: 60px; background: var(--card-navy); }
  .card-back { left: 80px; top: 400px; background: var(--card-black); }

  .brand {
    display: flex;
    align-items: center;
    gap: 12px;
    color: var(--ink-white);
    font-weight: 900;
    text-transform: uppercase;
    letter-spacing: 0.5px;
  }
  .brand-mark {
    width: 18px; height: 18px;
    border: 3px solid var(--ink-white);
  }
  .card-front .brand {
    position: absolute; left: 0; right: 0; top: 138px;
    justify-content: center; font-size: 28px;
  }
  .card-back .brand {
    position: absolute; right: 42px; top: 120px; font-size: 24px;
  }

  .holder { position: absolute; left: 42px; top: 38px; color: var(--ink-white); }
  .holder-name { font-weight: 700; font-style: italic; font-size: 17px; text-transform: uppercase; }
  .holder-role { font-size: 11px; color: var(--ink-muted); margin-top: 2px; }

  .contacts {
    position: absolute; left: 42px; top: 170px;
    list-style: none; color: var(--ink-soft); font-size: 15px; line-height: 22px;
  }
  .contacts li { display: flex; align-items: center; gap: 8px; }
  .contacts svg { width: 13px; height: 13px; flex: none; }
  .social-dot { width: 11px; height: 11px; border-radius: 50%; background: var(--ink-soft); flex: none; }

  .roles {
    position: absolute; right: 42px; top: 210px;
    list-style: none; text-align: right; color: var(--ink-soft);
    font-size: 15px; line-height: 21px;
  }
  .roles li::after {
    content: ""; display: inline-block; width: 7px; height: 7px;
    border-radius: 50%; background: var(--ink-white); margin-left: 8px; vertical-align: middle;
  }
</style>
</head>
<body>
  <section class="card card-front" aria-label="Card front">
    <div class="brand"><span class="brand-mark"></span>Dravelin Consulting</div>
  </section>

  <section class="card card-back" aria-label="Card back">
    <div class="holder">
      <p class="holder-name">Calder Wynn</p>
      <p class="holder-role">CEO</p>
    </div>

    <ul class="contacts">
      <li>
        <svg viewBox="0 0 16 16" aria-hidden="true"><path fill="#d6d6d6" d="M3 1l3 3-1.5 2a9 9 0 0 0 5.5 5.5L12 10l3 3-2 2C7 15 1 9 1 3z"/></svg>
        044-987 650 312
      </li>
      <li>
        <svg viewBox="0 0 16 16" aria-hidden="true"><rect x="1" y="3" width="14" height="10" fill="#d6d6d6"/><path d="M1 3l7 6 7-6" fill="none" stroke="#161616" stroke-width="1.5"/></svg>
        info@dravelinmail.com
      </li>
      <li><span class="social-dot"></span>@dravelinconsulting</li>
      <li><span class="social-dot"></span>@dravelinconsulting</li>
    </ul>

    <div class="brand"><span class="brand-mark"></span>Dravelin Consulting</div>

    <ul class="roles">
      <li>ICO Advisor</li>
      <li>World Champion Gamer</li>
      <li>Esports Award Winner</li>
      <li>Quorvane Expert</li>
    </ul>
  </section>
</body>
</html>
```